Business Card Design and Logo Needed

I need Business Cards and a Logo for my website and public speaking business which can be found at: www.kelsa-thorn.example

I'm looking for creative and unique ideas. Some business cards I've found online that I like can be found at:
http://gigplatelo.example/general/18-smokin-hot-business-card-designs/

and at

http://www.vortaplume.example/2009/04/50-creative-business-cards-of-50-graphic-designers/

```html
<!DOCTYPE html>
<html lang="en">
<head>
<meta charset="utf-8">
<title>Kelsa Thorn – Business Card</title>
<link rel="stylesheet" href="https://fonts.googleapis.com/css2?family=Arimo:ital,wght@0,400;1,400&display=swap">
<style>
  :root {
    --page: #ffffff;
    --card-brown: #6f4727;
    --pattern-brown: #7a5131;
    --lime: #8dc63f;
    --lime-2: #84b23e;
    --lime-3: #7c9d3c;
    --lime-4: #74893a;
    --lime-5: #6d6f34;
    --white: #ffffff;
  }
  * { margin: 0; padding: 0; box-sizing: border-box; }
  html, body {
    width: 1200px;
    height: 1124px;
    overflow: hidden;
    background: var(--page);
    font-family: "Arimo", Arial, sans-serif;
  }
  .canvas { position: relative; width: 1200px; height: 1124px; }

  .card {
    position: absolute;
    top: 90px;
    width: 460px;
    height: 922px;
    border-radius: 40px;
    background: var(--card-brown);
    color: var(--white);
    overflow: hidden;
  }
  .card--front { left: 31px; }
  .card--back { left: 630px; }

  .card__pattern {
    position: absolute;
    inset: 0;
    background: linear-gradient(180deg, var(--pattern-brown), var(--card-brown) 60%, var(--pattern-brown));
    opacity: 0.6;
  }

  .brand-mark {
    position: absolute;
    left: 138px;
    top: 150px;
    width: 184px;
    height: 184px;
  }

  .name {
    position: absolute;
    font-weight: 400;
    font-size: 68px;
    line-height: 78px;
    letter-spacing: -1px;
    color: var(--white);
    white-space: nowrap;
  }
  .name__accent { color: var(--lime); }
  .role {
    position: absolute;
    font-style: italic;
    font-size: 20px;
    line-height: 24px;
    letter-spacing: 1px;
    color: var(--white);
    white-space: nowrap;
  }
  .card--front .name { left: 34px; top: 447px; }
  .card--front .role { right: 32px; top: 519px; }
  .card--back .name { left: 39px; top: 274px; }
  .card--back .role { right: 28px; top: 348px; }

  .motto {
    position: absolute;
    left: 31px;
    top: 736px;
    list-style: none;
  }
  .motto li {
    font-size: 17px;
    letter-spacing: 4.6px;
    line-height: 29px;
    white-space: nowrap;
  }
  .motto li:nth-child(1) { color: var(--lime); }
  .motto li:nth-child(2) { color: var(--lime-2); }
  .motto li:nth-child(3) { color: var(--lime-3); }
  .motto li:nth-child(4) { color: var(--lime-4); }
  .motto li:nth-child(5) { color: var(--lime-5); }

  .contact {
    position: absolute;
    left: 0;
    right: 0;
    top: 470px;
    list-style: none;
    text-align: center;
    font-size: 24px;
    letter-spacing: 0.5px;
    line-height: 46.5px;
    color: var(--white);
  }
</style>
</head>
<body>
<main class="canvas">
  <section class="card card--front">
    <svg class="brand-mark" viewBox="0 0 184 184" aria-hidden="true">
      <circle cx="92" cy="92" r="90" fill="var(--lime)"/>
    </svg>
    <h1 class="name">Kelsa<span class="name__accent">Thorn</span></h1>
    <p class="role">Speaker, Philanthropist, Author</p>
    <ul class="motto">
      <li>Wonder. Explore. Dream. Achieve.</li>
      <li>Wonder. Explore. Dream. Achieve.</li>
      <li>Wonder. Explore. Dream. Achieve.</li>
      <li>Wonder. Explore. Dream. Achieve.</li>
      <li>Wonder. Explore. Dream. Achieve.</li>
    </ul>
  </section>

  <section class="card card--back">
    <div class="card__pattern" role="img" aria-label="Faint tone-on-tone repeating brand pattern"></div>
    <h2 class="name">Kelsa<span class="name__accent">Thorn</span></h2>
    <p class="role">Speaker, Philanthropist, Author</p>
    <ul class="contact">
      <li>YourCompanyName</li>
      <li>1234 Anywhere Avenue</li>
      <li>Suite #0000</li>
      <li>City, State 00000-0000</li>
      <li>Country</li>
      <li>Tel 000 000-0000</li>
      <li>Fax 000 000-0000</li>
      <li>Cel 000 000-0000</li>
      <li>your_name@quillmere.example</li>
    </ul>
  </section>
</main>
</body>
</html>
```